Thermostat Screen Design

We need a screen layout design for a new thermostat we're currently developing. If you're not familiar with thermostats, you can see some examples here - http://smart-climate-units-guide.bestpickdigest.com/

We're after the main page design, with icons, colours etc. It needs to be clean, modern and minimalistic. Attached is all components required on the screen. The screen size is 5 inch (diagnol).

The arrows on the screen showcase what happens when you press a button. For example, when you press MODE once you get OFF, press it twice, HEAT, press it 3 times, COOL, etc. This is just for your reference.

You have complete creative license on how you choose to layout the screen, position the components etc, but we require:

- it must be on a 5 inch screen diagnol
- modern, clean and minimalistic
- includes icons and colours
- Intuitive

Let me know if any questions.

```html
<!DOCTYPE html>
<html lang="en">
<head>
<meta charset="utf-8">
<title>Thermostat Main Screen</title>
<link href="https://fonts.googleapis.com/css2?family=Lato:wght@100;300;400;700&display=swap" rel="stylesheet">
<style>
  :root {
    --page-bg: #116fae;
    --screen-bg: #1670b0;
    --panel-bg: #3a89c2;
    --panel-row: #4a93c6;
    --divider: #2e7cb6;
    --sidebar-bg: #d8edf7;
    --sidebar-active: #c6dde9;
    --sidebar-line: #bcd6e4;
    --icon-blue: #1b6fae;
    --label-muted: #7da7c4;
    --white: #ffffff;
    --clock-bg: #3f8cc4;
    --clock-am: #bcd9ee;
  }
  * { box-sizing: border-box; margin: 0; padding: 0; }
  html, body { width: 1024px; height: 1200px; overflow: hidden; }
  body {
    background: var(--page-bg);
    font-family: "Lato", sans-serif;
    color: var(--white);
    position: relative;
  }
  .screen {
    position: absolute;
    left: 22px; top: 324px;
    width: 980px; height: 552px;
    background: var(--screen-bg);
    overflow: hidden;
  }
  .sidebar {
    position: absolute; left: 0; top: 0;
    width: 138px; height: 552px;
    background: var(--sidebar-bg);
  }
  .nav-item {
    height: 138px;
    display: flex; flex-direction: column; align-items: center; justify-content: center;
    border-bottom: 1px solid var(--sidebar-line);
    color: var(--label-muted);
    font-size: 23px; font-weight: 400;
    gap: 10px;
  }
  .nav-item:last-child { border-bottom: none; }
  .nav-item.is-active { background: var(--sidebar-active); }
  .nav-item svg { display: block; }

  .pill {
    position: absolute;
    border: 2px solid var(--white);
    border-radius: 4px;
    display: flex; align-items: center; justify-content: center;
    font-size: 19px; font-weight: 400;
  }
  .pill-small { font-size: 18px; }
  .pill-status { font-size: 22px; }
  .date-pill { gap: 10px; font-size: 19px; border-radius: 3px; }

  .temp-panel {
    position: absolute; left: 181px; top: 66px;
    width: 383px; height: 390px;
    background: var(--panel-bg);
  }
  .temp-label {
    position: absolute; top: 18px; left: 0; width: 100%;
    text-align: center; font-size: 24px; font-weight: 700;
  }
  .temp-value {
    position: absolute; top: 28px; left: 78px;
    font-size: 226px; font-weight: 100; line-height: 1;
    letter-spacing: -6px;
  }
  .temp-degree {
    position: absolute; top: 64px; left: 316px;
    font-size: 40px; font-weight: 300;
  }
  .setpoint {
    position: absolute; left: 0; width: 383px; height: 54px;
    display: flex; align-items: center;
    border-top: 1px solid var(--divider);
    background: var(--panel-row);
  }
  .setpoint-cool { top: 284px; }
  .setpoint-heat { top: 338px; background: var(--panel-bg); }
  .setpoint-text {
    width: 318px; display: flex; align-items: center; justify-content: center; gap: 8px;
    font-size: 23px; color: var(--icon-blue);
  }
  .setpoint-text strong { color: var(--white); font-size: 31px; font-weight: 700; margin-left: 10px; }
  .setpoint-arrow {
    width: 65px; height: 100%;
    border-left: 2px solid var(--divider);
    display: flex; align-items: center; justify-content: center;
  }

  .clock {
    position: absolute; left: 609px; top: 127px;
    width: 318px; height: 318px; border-radius: 50%;
    background: var(--clock-bg);
    text-align: center;
  }
  .clock-time {
    margin-top: 96px;
    font-size: 92px; font-weight: 300; line-height: 1; letter-spacing: -2px;
  }
  .clock-period { font-size: 36px; font-weight: 400; color: var(--clock-am); margin-top: 2px; }

  .action {
    position: absolute; top: 485px; height: 56px;
    border: 2px solid var(--white); border-radius: 4px;
    display: flex; align-items: center; justify-content: center; gap: 8px;
    font-size: 30px; font-weight: 400;
  }
</style>
</head>
<body>
<main class="screen">
  <nav class="sidebar">
    <div class="nav-item">
      <svg width="66" height="52" viewBox="0 0 66 52" aria-hidden="true">
        <g stroke="#1b6fae" stroke-width="3.5" stroke-linecap="round">
          <line x1="22" y1="4" x2="22" y2="36"/><line x1="8" y1="12" x2="36" y2="28"/><line x1="8" y1="28" x2="36" y2="12"/>
        </g>
        <path d="M48 22 C56 30 62 36 58 44 C55 50 44 51 40 44 C37 38 41 34 43 30 C44 34 47 35 48 32 C49 28 46 26 48 22Z" fill="#1b6fae"/>
      </svg>
      <span>Mode</span>
    </div>
    <div class="nav-item is-active">
      <svg width="58" height="58" viewBox="0 0 58 58" aria-hidden="true">
        <g fill="#1b6fae">
          <path d="M29 25 C22 14 26 3 36 4 C46 6 44 18 33 25Z"/>
          <path d="M33 31 C45 30 53 38 48 46 C42 54 33 46 31 35Z"/>
          <path d="M25 31 C19 42 8 44 5 36 C3 26 14 24 25 28Z"/>
          <circle cx="29" cy="29" r="5"/>
        </g>
      </svg>
      <span>Fan</span>
    </div>
    <div class="nav-item">
      <svg width="44" height="52" viewBox="0 0 44 52" aria-hidden="true">
        <g stroke="#1b6fae" stroke-width="3.5" stroke-linecap="round">
          <line x1="7" y1="3" x2="7" y2="49"/><line x1="22" y1="3" x2="22" y2="49"/><line x1="37" y1="3" x2="37" y2="49"/>
        </g>
        <g fill="#1b6fae"><rect x="1" y="16" width="12" height="9"/><rect x="16" y="30" width="12" height="9"/><rect x="31" y="10" width="12" height="9"/></g>
      </svg>
      <span>Settings</span>
    </div>
    <div class="nav-item">
      <svg width="58" height="40" viewBox="0 0 58 40" aria-hidden="true">
        <g fill="none" stroke="#1b6fae" stroke-width="3.5" stroke-linecap="round">
          <path d="M12 4 C2 14 2 26 12 36"/><path d="M20 12 C15 17 15 23 20 28"/>
          <path d="M46 4 C56 14 56 26 46 36"/><path d="M38 12 C43 17 43 23 38 28"/>
        </g>
      </svg>
      <span>Zones</span>
    </div>
  </nav>

  <div class="pill pill-small" style="left:185px;top:12px;width:197px;height:40px;">Outdoor Temp: 28°</div>
  <div class="pill pill-small" style="left:391px;top:12px;width:173px;height:40px;">Indoor RH: 20%</div>
  <div class="pill pill-status" style="left:608px;top:12px;width:146px;height:40px;">SLEEP</div>
  <div class="pill pill-status" style="left:780px;top:12px;width:147px;height:40px;">ZONE 1</div>
  <div class="pill date-pill" style="left:608px;top:66px;width:319px;height:38px;">
    <svg width="24" height="22" viewBox="0 0 24 22" aria-hidden="true">
      <rect x="1" y="3" width="22" height="18" fill="none" stroke="#bcd9ee" stroke-width="2"/>
      <line x1="1" y1="8" x2="23" y2="8" stroke="#bcd9ee" stroke-width="2"/>
      <line x1="6" y1="0" x2="6" y2="5" stroke="#bcd9ee" stroke-width="2"/><line x1="18" y1="0" x2="18" y2="5" stroke="#bcd9ee" stroke-width="2"/>
    </svg>
    <span>07-04-2014</span>
  </div>

  <section class="temp-panel">
    <div class="temp-label">Room Temp</div>
    <div class="temp-value">26</div>
    <div class="temp-degree">O</div>
    <div class="setpoint setpoint-cool">
      <div class="setpoint-text">
        <svg width="26" height="26" viewBox="0 0 26 26" aria-hidden="true"><g stroke="#1b6fae" stroke-width="3" stroke-linecap="round"><line x1="13" y1="2" x2="13" y2="24"/><line x1="3" y1="7.5" x2="23" y2="18.5"/><line x1="3" y1="18.5" x2="23" y2="7.5"/></g></svg>
        Cool Setpoint:<strong>68</strong>
      </div>
      <div class="setpoint-arrow"><svg width="26" height="16" viewBox="0 0 26 16" aria-hidden="true"><path d="M3 13 L13 3 L23 13" fill="none" stroke="#1b6fae" stroke-width="4.5"/></svg></div>
    </div>
    <div class="setpoint setpoint-heat">
      <div class="setpoint-text">
        <svg width="20" height="26" viewBox="0 0 20 26" aria-hidden="true"><path d="M10 1 C16 8 19 13 18 19 C17 24 12 26 9 25 C4 24 1 20 3 15 C4 12 6 10 7 8 C8 11 9 12 10 11 C11 8 9 5 10 1Z" fill="#1b6fae"/></svg>
        Heat Setpoint:<strong>74</strong>
      </div>
      <div class="setpoint-arrow"><svg width="26" height="16" viewBox="0 0 26 16" aria-hidden="true"><path d="M3 3 L13 13 L23 3" fill="none" stroke="#1b6fae" stroke-width="4.5"/></svg></div>
    </div>
  </section>

  <section class="clock">
    <div class="clock-time">09:26</div>
    <div class="clock-period">AM</div>
  </section>

  <div class="action" style="left:185px;width:183px;">Heat</div>
  <div class="action" style="left:381px;width:183px;">
    <svg width="36" height="36" viewBox="0 0 58 58" aria-hidden="true"><g fill="none" stroke="#bcd9ee" stroke-width="3.5"><path d="M29 25 C22 14 26 3 36 4 C46 6 44 18 33 25Z"/><path d="M33 31 C45 30 53 38 48 46 C42 54 33 46 31 35Z"/><path d="M25 31 C19 42 8 44 5 36 C3 26 14 24 25 28Z"/><circle cx="29" cy="29" r="5"/></g></svg>
    Auto
  </div>
  <div class="action" style="left:579px;width:183px;">
    <svg width="36" height="36" viewBox="0 0 26 26" aria-hidden="true"><g stroke="#bcd9ee" stroke-width="2.5" stroke-linecap="round"><line x1="13" y1="2" x2="13" y2="24"/><line x1="3" y1="7.5" x2="23" y2="18.5"/><line x1="3" y1="18.5" x2="23" y2="7.5"/></g></svg>
  </div>
  <div class="action" style="left:775px;width:183px;">Zone 1</div>
</main>
</body>
</html>
```